Media Services Start-up -- Corporate Website and Logo Design. Inspiration required!

We need a logo design and corporate website design, including coding, for our start-up business.
Brenvora’s value proposition is based on bringing together media content from a vast number of geographies globally, adding human and AI curation, translation and editing, and delivering the content using tailored customer interfaces. On the one hand, the business brings together media coverage from all over the world, and on the other it brings together content, human skills and technology to deliver a supreme customer experience.
Brenvora is a B2B media monitoring and analytics business with emphasis on global customers. Brenvora's service offering is centred around sourcing media content from different markets, processing, storing and delivering the content and insights derived from it using an online platform / mobile app.
The messaging we want to create through the logo is:
- Global scope
- Speed of delivery
- Cost-efficiency
- Multi-lingual
- Tailor-made
- Trustworthy
Target Market(s)
Business to business, PR / Communications, Media, Marketing
Logo Text
Brenvora
Coding
Coded - Design and coding required
Number of Pages Required
5+ page
Font styles to use
Other font styles liked:
- See Design Brief for details
Colors
Designer to choose colors to be used in the design.

```html
<!DOCTYPE html>
<html lang="en">
<head>
<meta charset="utf-8">
<title>Brenvora — Global Media Intelligence</title>
<link rel="stylesheet" href="https://fonts.googleapis.com/css2?family=Roboto:wght@400;500;700&family=Arimo:wght@400&display=swap">
<style>
  :root {
    --ink: #000000;
    --paper: #ffffff;
    --hero-dark: #0b1116;
    --hero-mid: #1f2a33;
    --hero-blue: #1d3f55;
    --field-border: #2b2b2b;
    --placeholder: #555555;
    --text-light: #ffffff;
  }
  * { margin: 0; padding: 0; box-sizing: border-box; }
  html, body { width: 1200px; height: 747px; overflow: hidden; background: var(--paper); }
  body { position: relative; font-family: "Roboto", sans-serif; color: var(--ink); }

  .site-header { position: absolute; top: 0; left: 0; width: 1200px; height: 71px; background: var(--paper); z-index: 3; }
  .brand { position: absolute; left: 141px; top: 15px; font-size: 29px; font-weight: 700; letter-spacing: 0.2px; }
  .main-nav a { position: absolute; top: 25px; font-size: 14px; color: var(--ink); text-decoration: none; }
  .btn-signin { position: absolute; left: 967px; top: 18px; width: 92px; height: 35px; background: var(--ink); color: var(--text-light);
    font-size: 15px; display: flex; align-items: center; justify-content: center; border-radius: 2px; box-shadow: 0 2px 6px rgba(0,0,0,.3); }

  .hero-visual { position: absolute; top: 71px; left: 0; width: 1200px; height: 648px; }

  .hero-copy { position: absolute; left: 140px; top: 265px; color: var(--text-light); z-index: 2; }
  .hero-title { font-size: 37px; font-weight: 700; line-height: 59px; letter-spacing: 0.3px; text-shadow: 0 2px 4px rgba(0,0,0,.6); }
  .hero-lead { margin-top: 20px; width: 460px; font-family: "Arimo", sans-serif; font-size: 15.5px; line-height: 25.4px; }

  .lead-card { position: absolute; left: 766px; top: 214px; width: 293px; height: 337px; background: var(--paper); border-radius: 5px; z-index: 2; }
  .lead-card svg.banner { position: absolute; left: 3px; top: 3px; }
  .lead-card h2 { position: absolute; left: 0; top: 18px; width: 100%; text-align: center; color: var(--text-light); font-size: 17px; font-weight: 500; }
  .field { position: absolute; left: 32px; width: 228px; height: 37px; border: 1px solid var(--field-border); border-radius: 3px;
    font-size: 12.5px; color: var(--placeholder); padding-left: 13px; display: flex; align-items: center; }
  .btn-start { position: absolute; left: 57px; top: 268px; width: 178px; height: 35px; background: var(--ink); color: var(--text-light);
    font-size: 15px; display: flex; align-items: center; justify-content: center; border-radius: 2px; }

  .site-footer .copyright { position: absolute; left: 141px; top: 715px; font-size: 12px; }
  .social { position: absolute; left: 951px; top: 714px; display: flex; gap: 5.6px; }
  .social span { width: 23px; height: 23px; border-radius: 50%; background: var(--ink); display: block; }
</style>
</head>
<body>
  <header class="site-header">
    <div class="brand">Brenvora</div>
    <nav class="main-nav">
      <a style="left:363px">Home</a>
      <a style="left:454px">Solutions</a>
      <a style="left:568px">How We Do It</a>
      <a style="left:707px">Our People</a>
      <a style="left:829px">Our Technology</a>
    </nav>
    <div class="btn-signin">SIGN IN</div>
  </header>

  <svg class="hero-visual" width="1200" height="648" viewBox="0 0 1200 648" role="img"
       aria-label="Photo of a business person holding a tablet over overlaid charts and social media icons">
    <defs>
      <linearGradient id="heroFill" x1="0" y1="0" x2="1" y2="1">
        <stop offset="0" stop-color="#2a3238"/>
        <stop offset="0.4" stop-color="var(--hero-dark)"/>
        <stop offset="0.7" stop-color="var(--hero-blue)"/>
        <stop offset="1" stop-color="var(--hero-mid)"/>
      </linearGradient>
    </defs>
    <polygon points="0,0 1200,0 1200,564 600,648 0,564" fill="url(#heroFill)"/>
  </svg>

  <section class="hero-copy">
    <h1 class="hero-title">DELIVERING GLOBAL MEDIA<br>INTELLIGENCE</h1>
    <p class="hero-lead">Brenvora is an international media intelligence service provider. We help communications teams builds and operate truly global media monitoring and measurement programmes.</p>
  </section>

  <form class="lead-card">
    <svg class="banner" width="287" height="60" viewBox="0 0 287 60">
      <path d="M0 5 Q0 0 5 0 H282 Q287 0 287 5 V39 L142 58 L0 39 Z" fill="var(--ink)"/>
    </svg>
    <h2>Learn More About Brenvora</h2>
    <div class="field" style="top:88px">Name</div>
    <div class="field" style="top:145px">Email Address</div>
    <div class="field" style="top:201px">Phone</div>
    <div class="btn-start">GET STARTED</div>
  </form>

  <footer class="site-footer">
    <p class="copyright">© 2019 Brenvora Analytics Media. All rights reserved.</p>
    <div class="social">
      <span aria-label="Social link"></span>
      <span aria-label="Social link"></span>
      <span aria-label="Social link"></span>
      <span aria-label="Feed link"></span>
    </div>
  </footer>
</body>
</html>
```